Business card for a "family office" company

Please provide professional looking business card designs, incorporating the attached logo and below details. Harrowmere Holdings Pty Ltd is a family office / financial investment company. We are looking for a modern, professional and contemporary card design.

Industry/Entity Type

Finance

Contact Information for Business Card

Name: Dean Malcott
Title: Director
Company: Harrowmere Holdings Pty Ltd
Email: harrowlead@ozmailnet.com.au
Mobile: 0492 635 718
Address: 3/412 Bramwood Parade, Ashcombe Rise WA 6097, Australia

Requirements
Must have
• All details above and the logo. logo only on back side. incorporate colours of logo
Nice to have
• up to you
Should not have
• ?

```html
<!DOCTYPE html>
<html lang="en">
<head>
<meta charset="utf-8">
<title>Harrowmere Holdings – Business Card</title>
<link rel="stylesheet" href="https://fonts.googleapis.com/css2?family=EB+Garamond:wght@400;500&display=swap">
<style>
  :root {
    --backdrop: #c9c9cb;
    --navy: #1e1d59;
    --ink-white: #ffffff;
    --ink-soft: #d6d5e8;
    --serif: "EB Garamond", Georgia, serif;
  }
  * { box-sizing: border-box; margin: 0; padding: 0; }
  html, body {
    width: 1200px; height: 960px; overflow: hidden;
    background: var(--backdrop);
    font-family: var(--serif);
  }
  .sheet {
    width: 1200px; height: 960px;
    display: flex; flex-direction: column; align-items: center; justify-content: center;
    gap: 60px;
  }
  .card {
    position: relative;
    width: 700px; height: 400px;
    background: var(--navy);
    color: var(--ink-white);
    box-shadow: 0 6px 18px rgba(0,0,0,0.25);
  }

  /* Brand wordmark */
  .brand { display: flex; align-items: center; gap: 14px; }
  .brand-square { width: 44px; height: 44px; background: currentColor; flex: none; }
  .brand-name { display: flex; flex-direction: column; line-height: 1; font-weight: 400; }
  .brand-name .main { font-size: 34px; letter-spacing: 0.06em; }
  .brand-name .sub { font-size: 13px; letter-spacing: 0.55em; margin-top: 6px; }

  /* Front */
  .card-front .brand { position: absolute; left: 40px; top: 120px; }
  .card-front .brand-name .main { font-size: 30px; }
  .divider {
    position: absolute; left: 350px; top: 70px;
    width: 2px; height: 290px; background: var(--ink-white);
  }
  .person { position: absolute; left: 388px; top: 62px; }
  .person-name {
    font-size: 38px; font-weight: 500; line-height: 1; letter-spacing: 0.04em;
    text-transform: uppercase;
  }
  .person-title { font-size: 24px; margin-top: 6px; }
  .contacts { position: absolute; left: 388px; top: 205px; list-style: none; }
  .contacts li {
    display: flex; align-items: flex-start; gap: 12px;
    font-size: 19px; line-height: 1.25; margin-bottom: 10px;
  }
  .contacts svg { width: 26px; height: 26px; flex: none; }

  /* Back */
  .card-back { display: flex; align-items: center; justify-content: center; color: var(--ink-soft); }
  .card-back .brand-square { width: 56px; height: 56px; }
  .card-back .brand-name .main { font-size: 40px; }
  .card-back .brand-name .sub { font-size: 15px; }
</style>
</head>
<body>
<main class="sheet">

  <section class="card card-front" aria-label="Business card front">
    <div class="brand">
      <span class="brand-square"></span>
      <span class="brand-name">
        <span class="main">HARROWMERE</span>
        <span class="sub">HOLDINGS</span>
      </span>
    </div>

    <div class="divider"></div>

    <div class="person">
      <p class="person-name">Dean<br>Malcott</p>
      <p class="person-title">Director</p>
    </div>

    <ul class="contacts">
      <li>
        <svg viewBox="0 0 26 26" aria-hidden="true">
          <rect x="1" y="1" width="24" height="24" rx="6" fill="#fff"/>
          <path d="M9 6c1 0 2 3 2 4s-1 1-1 2 3 4 4 4 1-1 2-1 4 1 4 2-2 3-3 3C11 20 6 15 6 9c0-1 2-3 3-3z" fill="#1e1d59"/>
        </svg>
        <span>0492 635 718</span>
      </li>
      <li>
        <svg viewBox="0 0 26 26" aria-hidden="true">
          <rect x="1" y="1" width="24" height="24" rx="6" fill="#fff"/>
          <rect x="6" y="8" width="14" height="10" fill="none" stroke="#1e1d59" stroke-width="1.4"/>
          <path d="M6 8l7 6 7-6" fill="none" stroke="#1e1d59" stroke-width="1.4"/>
        </svg>
        <span>harrowlead@ozmailnet.com.au</span>
      </li>
      <li>
        <svg viewBox="0 0 26 26" aria-hidden="true">
          <rect x="1" y="1" width="24" height="24" rx="6" fill="#fff"/>
          <path d="M13 5a6 6 0 0 1 6 6c0 4-6 10-6 10s-6-6-6-10a6 6 0 0 1 6-6z" fill="#1e1d59"/>
          <circle cx="13" cy="11" r="2.3" fill="#fff"/>
        </svg>
        <span>3/412 Bramwood Parade,<br>Ashcombe Rise WA 6097, Australia</span>
      </li>
    </ul>
  </section>

  <section class="card card-back" aria-label="Business card back">
    <div class="brand">
      <span class="brand-square"></span>
      <span class="brand-name">
        <span class="main">HARROWMERE</span>
        <span class="sub">HOLDINGS</span>
      </span>
    </div>
  </section>

</main>
</body>
</html>
```